Corbel Path Advisory WordPress Design

Corbel Path Advisory is a consulting company that targets small business. We use our genius in the field to help small Business navigate information systems, in particular Tallybridge Solutions.

We are looking for a WordPress Design that is playful but intelligent for our web site. The design should plays off of our Corbel Logo and be informative. The attachments is of our logo variations that will be used in your design. It should be useful to describe the look and feel of the site we are looking to get.

The color of the website is not defined yet but should work well with our logo colors.

Regarding to the template and the way to display the home page. The menu should contain the following items which will each be its own page:
1. Home Page
2. Blog
-This needs to be a frame work to allow us to constantly add written articles and Video logs with Transcripts possibly in two sections.
3. What Corbel Does
-This will contain the company approach
4. Request a Corbel
-This will be a form to collect contact information
5. Contact Corbel
6. About Us

Please keep the SIMILAR airy/mythical design used in the logo.

Finally, we need a design that will have a normal view and a mobile view.

Target Market(s)

Corbel Path Advisory is a consulting company that targets small business.

Industry/Entity Type

Business Consultant

Requirements
Must have
• Regarding to the template and the way to display the home page. The menu should contain the following items which will each be its own page:
• 1. Home Page
• 2. Blog
• -This needs to be a frame work to allow us to constantly add written articles and Video logs with Transcripts possibly in two sections.
• 3. What Corbel Does
• -This will contain the company approach
• 4. Request a Corbel
• -This will be a form to collect contact information
• 5. Contact Corbel
• 6. About Us
• Mobile View
Nice to have
• Have a magical or mythical quality like the hands around the logo but not to playful.
Should not have
• Our slogan is "Corbel solutions that make business work!"

```html
<!DOCTYPE html>
<html lang="en">
<head>
<meta charset="utf-8">
<title>Corbel Path Advisory</title>
<link rel="stylesheet" href="https://fonts.googleapis.com/css2?family=Open+Sans:wght@300;400;600;700;800&family=Oswald:wght@500;700&display=swap">
<style>
:root{
  --orange:#e8930f;
  --orange-dark:#c9760a;
  --orange-deep:#b96a07;
  --blue:#2c6fb9;
  --blue-dark:#1f5899;
  --blue-soft:#5b93d3;
  --ink:#3b3b3b;
  --muted:#7a7a7a;
  --paper:#ffffff;
  --mist:#eeeeee;
  --header-bg:#f3f4f7;
  --band:#dfe3ea;
}
*{box-sizing:border-box;margin:0;padding:0}
html,body{width:1200px;height:2328px;overflow:hidden}
body{font-family:"Open Sans",Arial,sans-serif;color:var(--ink);background:var(--paper);font-size:13px}
.wrap{width:872px;margin:0 auto;position:relative}

/* header */
.site-header{height:380px;background:linear-gradient(180deg,var(--band) 0,var(--band) 36px,var(--header-bg) 36px,var(--header-bg) 290px,var(--paper) 290px);display:flex;justify-content:center;padding-top:120px}
.brand{display:flex;align-items:center;gap:18px;height:120px}
.brand-dot{width:96px;height:96px;border-radius:50%;background:var(--blue);flex:none}
.brand-name{font-family:"Open Sans",sans-serif;font-weight:700;font-size:40px;color:var(--blue);line-height:1.05;width:290px}

/* nav */
.main-nav{height:44px;background:var(--orange);display:flex}
.main-nav a{color:#fff;text-decoration:none;font-size:14px;font-weight:600;text-transform:uppercase;padding:0 22px;line-height:44px;border-right:1px solid rgba(255,255,255,.25)}
.main-nav a.active{background:var(--orange-deep)}

/* hero */
.hero{height:464px;position:relative;overflow:hidden}
.hero-photo{position:absolute;inset:0;background:
  linear-gradient(90deg,rgba(40,40,44,.55) 0%,rgba(40,40,44,.1) 30%,rgba(255,255,255,0) 50%,rgba(40,40,44,.1) 72%,rgba(40,40,44,.55) 100%),
  linear-gradient(180deg,#dedfe1 0%,#b4b6ba 45%,#6d7075 100%)}
.hero-caption{position:absolute;left:370px;width:470px;top:322px;background:rgba(44,111,185,.88);color:#fff;text-align:center;padding:10px 0 12px}
.hero-caption small{display:block;font-size:20px;font-weight:300;line-height:1.3}
.hero-caption strong{display:block;font-size:26px;font-weight:400;line-height:1.25}
.hero-dots{position:absolute;top:432px;left:0;right:0;display:flex;justify-content:center;gap:8px}
.hero-dots span{width:12px;height:12px;border-radius:50%;background:#f5c04a}
.hero-dots span.on{background:var(--orange)}

/* feature services */
.features{height:290px;background:var(--mist)}
.features .wrap{display:flex;justify-content:space-between;padding-top:36px}
.feature{width:240px}
.feature svg{display:block;margin-bottom:12px}
.feature h3{font-size:26px;font-weight:300;line-height:1.15;color:#555}
.feature p{font-size:12px;color:var(--muted);line-height:1.45;margin:10px 0 14px}
.feature .tag{color:var(--orange);font-weight:700;font-size:12px;text-transform:uppercase;margin-top:4px;display:block}
.btn{display:inline-block;background:var(--orange);color:#fff;font-size:12px;font-weight:700;padding:8px 18px;text-transform:uppercase;text-decoration:none}
.btn.blue{background:var(--blue)}

/* welcome */
.welcome{height:170px;background:var(--paper);display:flex;align-items:center}
.welcome .wrap{border:1px solid #dcdcdc;height:136px;display:flex;align-items:center;padding:0 36px;gap:40px}
.welcome h1{font-family:"Oswald",sans-serif;font-weight:700;font-size:72px;color:var(--blue);letter-spacing:1px}
.welcome p{font-size:14px;color:var(--blue);font-weight:600;line-height:1.5;text-transform:uppercase}

/* content columns */
.content{height:380px}
.content .wrap{display:flex;justify-content:space-between;padding-top:24px}
.teach{width:300px}
.teach-top{display:flex;gap:18px}
.portrait{width:140px;height:170px;flex:none;background:linear-gradient(180deg,#e6e3df 0%,#b9aea6 55%,#5c5350 100%)}
.teach h2{font-size:26px;font-weight:400;line-height:1.2;color:#444;padding-top:8px}
.teach p{font-size:11px;color:var(--muted);line-height:1.45;margin-top:12px}
.col-title{font-size:32px;font-weight:300;color:#444;margin-bottom:10px}
.services-list{width:240px}
.services-list ul{list-style:none}
.services-list li{font-size:12.5px;font-weight:600;text-transform:uppercase;padding:4px 0 4px 16px;position:relative;color:#555}
.services-list li::before{content:"";position:absolute;left:0;top:11px;width:6px;height:6px;background:var(--orange)}
.services-list li.on{color:var(--orange)}
.news{width:260px}
.news-item{display:flex;gap:12px;margin-bottom:14px}
.news-date{width:54px;color:var(--orange);text-align:center;flex:none}
.news-date b{font-size:40px;font-weight:400;line-height:1;display:block}
.news-date small{font-size:11px;color:var(--muted)}
.news-item h4{color:var(--orange);font-size:15px;font-weight:400}
.news-item p{font-size:11px;color:var(--muted);line-height:1.4}

/* steps */
.steps{height:140px}
.steps .wrap{display:flex;justify-content:space-between;padding:8px 30px 0}
.step{width:110px;text-align:center}
.step-figure{width:92px;height:82px;border-radius:50% 50% 44% 44%;background:radial-gradient(ellipse at 50% 40%,var(--blue-soft) 0%,var(--blue) 60%,var(--blue-dark) 100%);margin:0 auto 12px}
.step span{font-size:12px;font-weight:600;text-transform:uppercase;color:#555}

/* quote */
.quote{height:150px;display:flex;align-items:center}
.quote .wrap{height:110px;border:1px solid #dcdcdc;background:#f7f7f7;display:flex;align-items:center;padding:0 26px;gap:22px}
.badge-24{width:78px;height:78px;border-radius:50%;border:3px solid #666;display:flex;align-items:center;justify-content:center;font-weight:800;font-size:26px;color:#444;flex:none}
.quote-text{flex:1}
.quote-text h3{font-size:24px;font-weight:400;color:#444}
.quote-text p{font-size:11px;color:var(--muted);line-height:1.4}
.quote .btn{padding:14px 22px;font-size:13px;flex:none}

/* footer */
.site-footer{height:262px;background:var(--orange)}
.site-footer .wrap{display:flex;padding-top:56px}
.foot-col{width:190px;list-style:none}
.foot-col li{color:#fff;font-size:13px;padding:5px 0 5px 18px;position:relative}
.foot-col li::before{content:"";position:absolute;left:0;top:12px;width:8px;height:8px;border-radius:50%;background:#fff}
.foot-brand{margin-left:auto;display:flex;align-items:center;gap:14px}
.foot-brand .brand-dot{width:60px;height:60px;background:#fff}
.foot-brand .brand-name{color:#fff;font-size:26px;width:190px}
.bottom-bar{height:48px;background:var(--orange-dark)}
.bottom-bar .wrap{display:flex;justify-content:space-between;align-items:center;height:48px;color:#fff;font-size:12px}
.social{display:flex;gap:8px}
.social span{width:22px;height:22px;border-radius:50%;background:rgba(255,255,255,.7)}
</style>
</head>
<body>

<header class="site-header">
  <div class="brand">
    <span class="brand-dot"></span>
    <span class="brand-name">Corbel Path Advisory</span>
  </div>
</header>

<nav class="wrap main-nav">
  <a class="active" href="#">Home</a>
  <a href="#">Blog</a>
  <a href="#">What Corbel Does</a>
  <a href="#">Request a Corbel</a>
  <a href="#">Contact Corbel</a>
  <a href="#">About Us</a>
</nav>

<section class="hero">
  <div class="hero-photo" role="img" aria-label="Black and white photo of business people meeting in an office with a chart screen"></div>
  <div class="hero-caption">
    <small>We Will Show You The Right</small>
    <strong>Direction To Your Business Success</strong>
  </div>
  <div class="hero-dots"><span class="on"></span><span></span><span></span><span></span><span></span></div>
</section>

<section class="features">
  <div class="wrap">
    <article class="feature">
      <svg width="34" height="30" viewBox="0 0 34 30"><rect x="2" y="16" width="7" height="12" fill="#666"/><rect x="13" y="8" width="7" height="20" fill="#666"/><rect x="24" y="2" width="7" height="26" fill="#666"/></svg>
      <h3>Finance<br>Management</h3>
      <span class="tag">Plan your money well</span>
      <p>Clear budgets, tidy books and simple reports so small teams always know where their cash goes.</p>
      <a class="btn" href="#">Read More</a>
    </article>
    <article class="feature">
      <svg width="34" height="30" viewBox="0 0 34 30"><circle cx="12" cy="9" r="6" fill="#666"/><path d="M2 28c0-7 5-11 10-11s10 4 10 11z" fill="#666"/><path d="M22 14l4 4 7-8" stroke="#666" stroke-width="3" fill="none"/></svg>
      <h3>Skills &amp;<br>Employment</h3>
      <span class="tag">Grow your people</span>
      <p>Hands-on training that helps staff use their systems with ease and confidence every single day.</p>
      <a class="btn" href="#">Read More</a>
    </article>
    <article class="feature">
      <svg width="34" height="30" viewBox="0 0 34 30"><circle cx="17" cy="15" r="13" fill="none" stroke="#666" stroke-width="3"/><path d="M4 15h26M17 2c-6 7-6 19 0 26M17 2c6 7 6 19 0 26" stroke="#666" stroke-width="2" fill="none"/></svg>
      <h3>Outsourcing<br>Programs</h3>
      <span class="tag">Work beyond walls</span>
      <p>Trusted remote help for the tasks that slow you down, so you can focus on your core work.</p>
      <a class="btn blue" href="#">Read More</a>
    </article>
  </div>
</section>

<section class="welcome">
  <div class="wrap">
    <h1>WELCOME!</h1>
    <p>We guide small businesses through their information systems with calm, clear and practical advice that makes work simpler.</p>
  </div>
</section>

<section class="content">
  <div class="wrap">
    <div class="teach">
      <div class="teach-top">
        <div class="portrait" role="img" aria-label="Photo of a smiling consultant in a dark suit"></div>
        <h2>We Will Teach You How To Implement!</h2>
      </div>
      <p>Step by step, we set up your Tallybridge workspace, move your files and show your team how to share, search and work together. We stay close until everything runs smoothly and each person feels at home with the tools.</p>
    </div>
    <div class="services-list">
      <h2 class="col-title">Our Services</h2>
      <ul>
        <li>Implementation</li>
        <li>SEO</li>
        <li class="on">SEO Marketing</li>
        <li>E-Commerce</li>
        <li>Sales and Marketing</li>
        <li>Exploit Your Ideas</li>
        <li>Market Sales</li>
        <li>Assessment Plan</li>
        <li>Syncing Sitemap</li>
        <li>Simple Workflows</li>
      </ul>
    </div>
    <div class="news">
      <h2 class="col-title">What's New</h2>
      <div class="news-item"><div class="news-date"><b>22</b><small>SEP 2014</small></div><div><h4>Fresh site launch</h4><p>Our new home page is live with guides, videos and easy ways to reach us.</p></div></div>
      <div class="news-item"><div class="news-date"><b>15</b><small>SEP 2014</small></div><div><h4>Free workshop</h4><p>Join a short session on sharing documents safely across small teams.</p></div></div>
      <div class="news-item"><div class="news-date"><b>09</b><small>SEP 2014</small></div><div><h4>New video logs</h4><p>Watch quick tips with full transcripts in our growing blog library.</p></div></div>
    </div>
  </div>
</section>

<section class="steps">
  <div class="wrap">
    <div class="step"><div class="step-figure" role="img" aria-label="Blue seated figure illustration for the examine step"></div><span>Examine</span></div>
    <div class="step"><div class="step-figure" role="img" aria-label="Blue seated figure illustration for the analyze step"></div><span>Analyze</span></div>
    <div class="step"><div class="step-figure" role="img" aria-label="Blue seated figure illustration for the identify step"></div><span>Identify</span></div>
    <div class="step"><div class="step-figure" role="img" aria-label="Blue seated figure illustration for the develop step"></div><span>Develop</span></div>
    <div class="step"><div class="step-figure" role="img" aria-label="Blue seated figure illustration for the succeed step"></div><span>Succeed</span></div>
  </div>
</section>

<section class="quote">
  <div class="wrap">
    <div class="badge-24">24h</div>
    <div class="quote-text">
      <h3>Have a question or need a custom quote?</h3>
      <p>Tell us about your business and goals. We reply within one day with a clear plan and a fair price for the work you need.</p>
    </div>
    <a class="btn blue" href="#">Get Started Now For Free</a>
  </div>
</section>

<footer class="site-footer">
  <div class="wrap">
    <ul class="foot-col"><li>Homepage</li><li>Blog</li><li>Solutions</li><li>Business Help</li></ul>
    <ul class="foot-col"><li>About Us</li><li>Testimonials</li><li>Our Team</li><li>Promotion</li></ul>
    <ul class="foot-col"><li>Contact Us</li><li>Education &amp; Training</li><li>Affiliate Program</li><li>Promotion</li></ul>
    <div class="foot-brand">
      <span class="brand-dot"></span>
      <span class="brand-name">Corbel Path Advisory</span>
    </div>
  </div>
</footer>
<div class="bottom-bar">
  <div class="wrap">
    <span>© 2014 | Corbel Path Advisory | All rights reserved</span>
    <div class="social"><span></span><span></span><span></span><span></span></div>
  </div>
</div>

</body>
</html>
```